Meridale Holding Partners Corporate Showcase

Provide an attractive Corporate Website for a boutique Investment Company to showcase our activities and corporate interests.

Our Company works across a number of Sectors including

Real Estate
E-Commerce
Healthcare
Beauty & Personal Care
Technology
Resources

Lets keep the personality

Modern
Global
Sophisticated
Calm
Interesting

Lets keep the pages with MINIMAL Words
Lets use Photos/ Imagery to tell the story

We'll need a Banner Menu -
About Us
Expertise
Global Outlook
Sectors
Management
Media
Contact Us

Many thanks
Best wishes
Derek.

Target Market(s)

Investors
Clients

Coding

Coded - Design and coding required

Number of Pages Required

5+ page

Font styles to use
Sans Serif

Colors
886aae
3176b5
00a990
f68e4d
f04a50
e667a6

Requirements
Must have
• WordPress Coding

Checkout this Website for look and feel - its cool:
www.kvr.com

Meridale Holding Stewardship
(Meridale Holding Partners LLP)
London
E4 2RL
United Kingdom

www.MeridaleHoldingStewardship.com
Nice to have
• Sophisticated colour palette - black/ brown/ blue/ purple/

```html
<!DOCTYPE html>
<html lang="en">
<head>
<meta charset="utf-8">
<title>Meridale Holding Partners</title>
<link href="https://fonts.googleapis.com/css2?family=Rubik:wght@400;500;600&family=Open+Sans:wght@400;600;700&display=swap" rel="stylesheet">
<style>
:root{
  --blue:#2f74b5;
  --blue-dark:#1f5e9c;
  --purple:#7f5ea9;
  --red:#f04a50;
  --gold:#f5b400;
  --ink:#2a2a2a;
  --muted:#777;
  --pale:#eef6fc;
  --line:#e3e3e3;
  --black:#141414;
}
*{box-sizing:border-box;margin:0;padding:0}
html,body{width:1200px;height:4688px;overflow:hidden}
body{font-family:"Open Sans",Arial,sans-serif;color:var(--ink);background:#fff;position:relative}
h1,h2,h3,h4,.rubik{font-family:"Rubik",Arial,sans-serif}
.wrap{width:1000px;margin:0 auto;position:relative}
.btn{display:inline-block;background:var(--purple);color:#fff;font-family:"Rubik",sans-serif;font-weight:500;font-size:14px;letter-spacing:.3px;padding:0 22px;height:42px;line-height:42px;text-transform:uppercase}
.label{font-size:12px;color:var(--blue);font-weight:600;text-transform:uppercase;letter-spacing:.3px}
.mark{display:inline-block;width:14px;height:14px;background:var(--blue)}
/* header */
.topbar{height:70px}
.topbar .wrap{display:flex;align-items:center;height:70px}
.logo{font-family:"Rubik",sans-serif;font-weight:600;font-size:30px;color:var(--blue);display:flex;align-items:center;gap:10px;text-transform:uppercase}
.logo .mark{width:20px;height:20px}
.top-right{margin-left:auto;display:flex;align-items:center;gap:14px}
.call{display:flex;align-items:center;gap:10px}
.call .ico{width:34px;height:34px;border-radius:50%;background:var(--purple);display:flex;align-items:center;justify-content:center}
.call small{display:block;font-size:10px;font-weight:600}
.call b{font-size:18px;font-weight:700}
.login{background:var(--purple);color:#fff;font-size:15px;font-family:"Rubik";padding:0 14px;height:34px;border-radius:3px;display:flex;align-items:center;gap:7px}
.search{width:120px;height:34px;border:1px solid var(--line);font-size:12px;padding:0 10px;line-height:32px;position:relative}
.search:after{content:"";position:absolute;right:10px;top:11px;width:9px;height:9px;border:1.5px solid #9ab;border-radius:50%}
.nav{background:var(--blue);height:48px}
.nav ul{display:flex;list-style:none;height:48px;align-items:center;width:1000px;margin:0 auto;justify-content:space-between}
.nav li{color:#fff;font-family:"Rubik";font-size:15px;text-transform:uppercase}
.nav li.sep{opacity:.8}
/* hero */
.hero{height:592px;position:relative;background:linear-gradient(120deg,#0e2c52 0%,#2d5d8e 35%,#a9bfd2 60%,#5a6f86 75%,#e08a3a 100%);text-align:center;color:#fff}
.hero h1{position:absolute;top:300px;left:0;right:0;font-size:44px;font-weight:500;line-height:54px;text-transform:uppercase;letter-spacing:.5px}
.hero p{position:absolute;top:414px;left:0;right:0;font-size:14px;line-height:22px}
.hero .btn{position:absolute;top:473px;left:525px;height:40px;line-height:40px;font-size:13px}
.arrow{position:absolute;top:50%;width:18px;height:18px;border-left:2px solid rgba(255,255,255,.8);border-bottom:2px solid rgba(255,255,255,.8)}
.arrow.l{left:70px;transform:translateY(-50%) rotate(45deg)}
.arrow.r{right:70px;transform:translateY(-50%) rotate(-135deg)}
.dots{position:absolute;top:542px;left:0;right:0;display:flex;justify-content:center;gap:7px}
.dots i{width:11px;height:11px;border-radius:50%;border:2px solid #fff}
.dots i.on{background:#fff}
/* about */
.about{height:450px;padding-top:78px}
.about .wrap{display:flex}
.about-intro{width:320px}
.about-intro .tag{display:flex;align-items:center;gap:10px}
.about-intro .tag .rule{width:36px;height:1px;background:var(--blue)}
.about-intro h2{color:var(--blue);font-size:28px;line-height:31px;font-weight:500;margin:14px 0 12px;white-space:nowrap;letter-spacing:-.2px}
.about-intro p{font-size:12.5px;color:var(--muted);line-height:22px;margin-bottom:22px;width:300px}
.pillars{display:flex;margin-left:28px;margin-top:26px;gap:0}
.pillar{width:237px}
.pillar svg{display:block;margin-bottom:10px}
.pillar h3{color:var(--blue);font-size:21px;font-weight:500;line-height:22px;margin-bottom:14px}
.pillar p{font-size:12.5px;color:var(--muted);line-height:21px;width:200px}
/* split band */
.band{height:379px;display:flex;position:relative;color:#fff}
.band .half{width:600px;height:379px;position:relative}
.band .left{background:linear-gradient(135deg,#3a7ec0,#2a68a8 60%,#2f74b5)}
.band .right{background:linear-gradient(135deg,#3d7fbd,#4f8ccc 50%,#2c6ead);border-left:2px solid #fff}
.band h2{font-size:31px;font-weight:400;position:absolute;top:88px}
.band p{position:absolute;top:148px;font-size:12.5px;line-height:23px;width:330px}
.band .btn{position:absolute;top:243px}
.band .left h2,.band .left p,.band .left .btn{left:100px}
.band .right h2,.band .right p,.band .right .btn{right:100px;text-align:right}
.band .hub{position:absolute;left:542px;top:130px;width:116px;height:116px;border-radius:50%;background:#fff;display:flex;align-items:center;justify-content:center}
.band .hub .mark{width:26px;height:26px}
/* sectors */
.sectors{height:1074px;padding-top:60px;text-align:center}
.sectors .mark,.media .mark,.testi .mark{display:block;margin:0 auto 14px}
.sectors h2{color:var(--blue);font-size:36px;font-weight:500;margin:10px 0 30px}
.grid{display:grid;grid-template-columns:repeat(3,315px);gap:23px 27px;text-align:left}
.card{height:374px;border:1px solid var(--line);position:relative}
.card .img{height:206px;position:relative}
.card .badge{position:absolute;right:0;bottom:0;width:62px;height:62px;background:var(--red);display:flex;align-items:center;justify-content:center}
.card h3{font-size:21px;font-weight:500;margin:20px 16px 10px}
.card p{font-size:12.5px;color:var(--muted);line-height:22px;margin:0 16px}
.more{font-family:"Rubik";font-size:14px;font-weight:500;color:var(--purple);text-transform:uppercase;position:absolute;left:16px;bottom:18px}
/* management */
.mgmt{height:546px;background:var(--pale);padding-top:91px}
.mgmt .wrap{display:flex;justify-content:space-between}
.mgmt .txt{width:460px}
.mgmt .tag{display:flex;align-items:center;gap:10px}
.mgmt .tag .rule{width:36px;height:1px;background:var(--blue)}
.mgmt h2{color:var(--blue);font-size:30px;font-weight:500;margin:10px 0 12px}
.mgmt p{font-size:12.5px;line-height:23px;color:var(--muted);margin-bottom:24px}
.mgmt .photo{width:481px;height:361px;margin-top:-2px;background:linear-gradient(160deg,#d8d4cf,#8d8a86 45%,#4d5a6a 75%,#c9c6c2)}
/* testimonials */
.testi{height:456px;background:linear-gradient(120deg,#3a7cbd,#2f74b5 50%,#3b7ebf);color:#fff;text-align:center;padding-top:68px;position:relative}
.testi .mark{background:#fff}
.testi .label{color:#fff}
.testi h2{font-size:34px;font-weight:500;margin:6px 0 30px}
.quotes{display:flex;justify-content:space-between;width:1000px;margin:0 auto}
.quote{width:318px}
.quote .qm{font-family:"Rubik";font-size:58px;line-height:38px;height:34px;font-weight:600}
.quote .stars{color:var(--gold);font-size:18px;letter-spacing:1px;margin:4px 0 4px}
.quote p{font-size:14.5px;line-height:24px}
.quote b{display:block;font-size:15px;margin-top:6px;font-weight:700}
.testi .arrow{top:270px;width:20px;height:20px}
/* media */
.media{height:692px;padding-top:48px;text-align:center}
.media h2{color:var(--blue);font-size:30px;font-weight:500;margin:8px 0 22px}
.mgrid{display:grid;grid-template-columns:repeat(3,315px);gap:27px;text-align:left}
.mcard{position:relative;height:430px}
.mbox{height:362px;border:1px solid var(--line)}
.mbox h3{color:var(--blue);font-size:21px;font-weight:500;padding:14px 16px 10px}
.mbox .img{height:205px}
.mbox h4{color:var(--blue);font-size:19px;font-weight:400;margin:16px 16px 8px}
.mbox p{font-size:12.5px;line-height:22px;color:var(--muted);margin:0 16px}
.mcard .more{bottom:14px}
/* footer */
.foot{height:381px;background:var(--black);color:#fff;padding-top:78px;position:relative}
.foot .wrap{display:flex}
.foot h5{font-family:"Rubik";font-size:14px;font-weight:500;text-transform:uppercase;margin-bottom:10px}
.signup{width:318px}
.row{display:flex;gap:4px;margin-bottom:6px}
.field{background:#fff;color:#777;font-size:11px;height:38px;line-height:38px;padding:0 8px;flex:1}
.signup .btn{width:100%;text-align:center;height:40px;line-height:40px;font-size:13px}
.links{padding-left:34px;border-left:1px solid #333;margin-left:34px}
.links.s2{border:0;margin-left:0;padding-left:50px;padding-right:36px;border-right:1px solid #333}
.links li{list-style:none;font-size:13px;line-height:25px}
.brand{margin-left:auto;width:240px;text-align:center;padding-top:52px}
.brand .logo{color:#fff;justify-content:center;font-size:34px}
.brand .logo .mark{background:#fff}
.social{display:flex;gap:8px;justify-content:center;margin-top:28px}
.social i{width:34px;height:34px;border:1.5px solid #fff;border-radius:50%}
.copy{position:absolute;left:0;right:0;bottom:0;height:56px;border-top:1px solid #2c2c2c;text-align:center;line-height:54px;font-size:14px}
</style>
</head>
<body>

<header class="topbar">
  <div class="wrap">
    <div class="logo"><span class="mark"></span>Meridale</div>
    <div class="top-right">
      <div class="call">
        <span class="ico"><svg width="16" height="16" viewBox="0 0 24 24"><path fill="#fff" d="M6.6 10.8a15 15 0 0 0 6.6 6.6l2.2-2.2a1 1 0 0 1 1-.25 11.4 11.4 0 0 0 3.6.6 1 1 0 0 1 1 1V20a1 1 0 0 1-1 1A17 17 0 0 1 3 4a1 1 0 0 1 1-1h3.5a1 1 0 0 1 1 1c0 1.25.2 2.45.6 3.6a1 1 0 0 1-.25 1z"/></svg></span>
        <div><small>Call Us</small><b>555-014-2290</b></div>
      </div>
      <div class="login"><svg width="12" height="14" viewBox="0 0 12 14"><circle cx="6" cy="3.5" r="3.2" fill="#fff"/><path d="M0 14c0-4 2.7-6 6-6s6 2 6 6z" fill="#fff"/></svg>Login</div>
      <div class="search">Search</div>
    </div>
  </div>
</header>

<nav class="nav">
  <ul>
    <li>Home</li><li class="sep">|</li><li>About Us</li><li class="sep">|</li><li>Expertise</li><li class="sep">|</li><li>Global Outlook</li><li class="sep">|</li><li>Sectors</li><li class="sep">|</li><li>Management</li><li class="sep">|</li><li>Media</li><li class="sep">|</li><li>Contact Us</li>
  </ul>
</nav>

<section class="hero" role="img" aria-label="Glass skyscrapers seen from below against a cloudy sky with warm sunlight">
  <span class="arrow l"></span><span class="arrow r"></span>
  <h1>Exclusive Access To<br>Premium Investments</h1>
  <p>Lorem ipsum dolor sit amet, consectetur adipiscing elit, sed<br>do eiusmod tempor incididunt ut labore</p>
  <span class="btn">Get Started &raquo;</span>
  <div class="dots"><i class="on"></i><i></i><i></i><i></i></div>
</section>

<section class="about">
  <div class="wrap">
    <div class="about-intro">
      <div class="tag"><span class="mark"></span><span class="rule"></span><span class="label">About Us</span></div>
      <h2>We Are Specialized<br>Capital Investments<br>Corporate</h2>
      <p>Lorem ipsum do consectetur adipiscig el, seo eiusmod tempo incididunt consectetur adipiscing elit, seo eiusmod tempor</p>
      <span class="btn">Learn More &raquo;</span>
    </div>
    <div class="pillars">
      <div class="pillar">
        <svg width="64" height="60" viewBox="0 0 64 60" fill="none" stroke="#2f74b5" stroke-width="2.5"><circle cx="30" cy="32" r="24"/><circle cx="30" cy="32" r="15"/><circle cx="30" cy="32" r="6"/><path d="M30 32 56 8M50 6v8h8"/></svg>
        <h3>Mission<br>&amp; Values</h3>
        <p>Lorem ipsum do consectetur adipiscing elit, seo eiusmod tempor incididunt</p>
      </div>
      <div class="pillar">
        <svg width="64" height="60" viewBox="0 0 64 60" fill="none" stroke="#2f74b5" stroke-width="2.5"><path d="M20 56h28M22 50h24l-3-18H25zM26 32l2-12h12l2 12M28 20V8h12v12"/></svg>
        <h3>Investment<br>Strategy</h3>
        <p>Lorem ipsum do consectetur adipiscing elit, seo eiusmod tempor incididunt</p>
      </div>
      <div class="pillar">
        <svg width="64" height="60" viewBox="0 0 64 60" fill="none" stroke="#2f74b5" stroke-width="2.5"><path d="M8 54h40M12 54V40h6v14M22 54V32h6v14M32 54V26h6v28M10 30 30 14l8 6 14-14"/><circle cx="50" cy="44" r="9"/></svg>
        <h3>Responsible<br>Investing</h3>
        <p>Lorem ipsum do consectetur adipiscing elit, seo eiusmod tempor incididunt</p>
      </div>
    </div>
  </div>
</section>

<section class="band">
  <div class="half left" role="img" aria-label="Blue-tinted financial charts and digital data behind the expertise panel">
    <h2>Expertise</h2>
    <p>Lorem ipsum dolor sit amet, consectetur adipisg elit, sed do eiusmod tempor incididunt ut labore et dolore magna aliqua. Quis ipsum suspendisse ultrices</p>
    <span class="btn">Learn More &raquo;</span>
  </div>
  <div class="half right" role="img" aria-label="Blue-tinted office scene of a business meeting behind the global outlook panel">
    <h2>Global Outlook</h2>
    <p>Lorem ipsum dolor sit amet, consectetur adipisg elit, sed do eiusmod tempor incididunt ut labore et dolore magna aliqua. Quis ipsum suspendisse ultrices</p>
    <span class="btn">Learn More &raquo;</span>
  </div>
  <div class="hub"><span class="mark"></span></div>
</section>

<section class="sectors">
  <span class="mark"></span>
  <div class="label">Our Sectors</div>
  <h2>We Are Specialised In</h2>
  <div class="wrap grid">
    <article class="card"><div class="img" role="img" aria-label="Laptop with small house models for real estate" style="background:linear-gradient(135deg,#2a6f93,#7fb2c8 50%,#1e4e6b)"><span class="badge"><svg width="30" height="30" fill="none" stroke="#fff" stroke-width="2"><path d="M4 14 15 5l11 9M7 12v13h16V12"/></svg></span></div><h3>Real Estate</h3><p>Lorem ipsum dolor sit amet, conse adipiscing elit, sed do eiusmod tempor iididunt ut labore et dolore magna aliqua.</p><span class="more">Learn More &raquo;</span></article>
    <article class="card"><div class="img" role="img" aria-label="Laptop with shopping cart and parcels for e-commerce" style="background:linear-gradient(135deg,#c9b7d8,#5b4f9a 45%,#d9cfc6)"><span class="badge"><svg width="30" height="30" fill="none" stroke="#fff" stroke-width="2"><rect x="5" y="6" width="20" height="14"/><path d="M11 25h8M15 20v5"/></svg></span></div><h3>E-Commerce</h3><p>Lorem ipsum dolor sit amet, conse adipiscing elit, sed do eiusmod tempor iididunt ut labore et dolore magna aliqua.</p><span class="more">Learn More &raquo;</span></article>
    <article class="card"><div class="img" role="img" aria-label="Stethoscope resting on a heart rhythm chart for healthcare" style="background:linear-gradient(135deg,#eef3f7,#b9d3e6 55%,#e4ecf2)"><span class="badge"><svg width="30" height="30" fill="none" stroke="#fff" stroke-width="2"><path d="M15 25S5 18 5 11a5 5 0 0 1 10-1 5 5 0 0 1 10 1c0 7-10 14-10 14z"/></svg></span></div><h3>Healthcare</h3><p>Lorem ipsum dolor sit amet, conse adipiscing elit, sed do eiusmod tempor iididunt ut labore et dolore magna aliqua.</p><span class="more">Learn More &raquo;</span></article>
    <article class="card"><div class="img" role="img" aria-label="Spa treatment scene with towels and petals for beauty and personal care" style="background:linear-gradient(135deg,#f1e4dc,#d9a89a 50%,#f4ece6)"><span class="badge"><svg width="30" height="30" fill="none" stroke="#fff" stroke-width="2"><rect x="7" y="10" width="16" height="15"/><path d="M11 10V5h8v5"/></svg></span></div><h3>Beauty &amp; Personal Care</h3><p>Lorem ipsum dolor sit amet, conse adipiscing elit, sed do eiusmod tempor iididunt ut labore et dolore magna aliqua.</p><span class="more">Learn More &raquo;</span></article>
    <article class="card"><div class="img" role="img" aria-label="Robot beside glowing formulas for technology" style="background:linear-gradient(135deg,#0d1e3a,#2b4f7c 55%,#0a1a30)"><span class="badge"><svg width="30" height="30" fill="none" stroke="#fff" stroke-width="2"><circle cx="15" cy="15" r="5"/><path d="M15 4v5M15 21v5M4 15h5M21 15h5"/></svg></span></div><h3>Technology</h3><p>Lorem ipsum dolor sit amet, conse adipiscing elit, sed do eiusmod tempor iididunt ut labore et dolore magna aliqua.</p><span class="more">Learn More &raquo;</span></article>
    <article class="card"><div class="img" role="img" aria-label="Colleagues reviewing printed charts at a desk for resources" style="background:linear-gradient(135deg,#3a4a66,#9aa6b8 50%,#dfe3ea)"><span class="badge"><svg width="30" height="30" fill="none" stroke="#fff" stroke-width="2"><circle cx="10" cy="10" r="4"/><circle cx="21" cy="10" r="4"/><path d="M3 25c0-5 3-8 7-8s7 3 7 8M14 25c0-5 3-8 7-8s6 3 6 8"/></svg></span></div><h3>Resources</h3><p>Lorem ipsum dolor sit amet, conse adipiscing elit, sed do eiusmod tempor iididunt ut labore et dolore magna aliqua.</p><span class="more">Learn More &raquo;</span></article>
  </div>
</section>

<section class="mgmt">
  <div class="wrap">
    <div class="txt">
      <div class="tag"><span class="mark"></span><span class="rule"></span><span class="label">Lorem Ipsum</span></div>
      <h2>Meridale Management</h2>
      <p>Sed ut perspiciatis unde omnis iste natus error sit voluptatem accusantium doloremque laudantium, totam rem aperiam, eaque ipsa quae ab inventore veritatis et quasi architecto beatae vitae dicta sunt explibo. Nu enim ipsam voluptatem quia voluptas sit aspernatur aut odit aut fugitqua consequuntur magni dolores eos qui ratione voluptatem sequi nesciunt. Nu oro quisquam est, qui dolorem ipsum quia dolor sit amet, consectetur, adipici vit, sed quia non numquam eius modi tempora incidunt ut labore etore magnam aliquam quaerat voluptatem. Ut enim ad minima veniam, quis nom exercitationem ullam corporis suscipit laboriosam</p>
      <span class="btn">Learn More &raquo;</span>
    </div>
    <div class="photo" role="img" aria-label="Group photo of the management team standing in a bright brick-walled office"></div>
  </div>
</section>

<section class="testi">
  <span class="mark"></span>
  <div class="label">Testimonial</div>
  <h2>What Our Customers Say</h2>
  <span class="arrow l"></span><span class="arrow r"></span>
  <div class="quotes">
    <div class="quote"><div class="qm">&ldquo;</div><div class="stars">&#9733;&#9733;&#9733;&#9733;&#9733;</div><p>Lorem ipsum dolor sit amet, consectetur adipiscing elit, sed do eiusmod tempor Lorem ipsum dolor sit amet,</p><b>- Clara Whitfield</b></div>
    <div class="quote"><div class="qm">&ldquo;</div><div class="stars">&#9733;&#9733;&#9733;&#9733;&#9733;</div><p>Lorem ipsum dolor sit amet, consectetur adipiscing elit, sed do eiusmod tempor Lorem ipsum dolor sit amet,</p><b>- Clara Whitfield</b></div>
    <div class="quote"><div class="qm">&ldquo;</div><div class="stars">&#9733;&#9733;&#9733;&#9733;&#9733;</div><p>Lorem ipsum dolor sit amet, consectetur adipiscing elit, sed do eiusmod tempor Lorem ipsum dolor sit amet,</p><b>- Clara Whitfield</b></div>
  </div>
</section>

<section class="media">
  <span class="mark"></span>
  <div class="label">Our Media</div>
  <h2>Meridale Holding Partners Media Center</h2>
  <div class="wrap mgrid">
    <article class="mcard"><div class="mbox"><h3>Press Releases</h3><div class="img" role="img" aria-label="House models and coin stacks beside a calculator" style="background:linear-gradient(135deg,#f3ede2,#c9b08a 50%,#eee7dc)"></div><h4>The standard Lorem Ipsum</h4><p>Lorem ipsum dolor sit amet, conse adipiscing elit, sed do eiusmod tempor</p></div><span class="more">About Companies &raquo;</span></article>
    <article class="mcard"><div class="mbox"><h3>MHP In The News</h3><div class="img" role="img" aria-label="Businessman working at a laptop in a dim office" style="background:linear-gradient(135deg,#2b2b2b,#6d6458 50%,#c7b9a6)"></div><h4>The standard Lorem Ipsum</h4><p>Lorem ipsum dolor sit amet, conse adipiscing elit, sed do eiusmod tempor</p></div><span class="more">More News &raquo;</span></article>
    <article class="mcard"><div class="mbox"><h3>MHP Events</h3><div class="img" role="img" aria-label="Tablet showing a glowing growth chart at an evening event" style="background:linear-gradient(135deg,#101a2e,#3a4a78 50%,#9a6b4a)"></div><h4>The standard Lorem Ipsum</h4><p>Lorem ipsum dolor sit amet, conse adipiscing elit, sed do eiusmod tempor</p></div><span class="more">More Events &raquo;</span></article>
  </div>
</section>

<footer class="foot">
  <div class="wrap">
    <div class="signup">
      <h5>Get Insights &amp; Updates</h5>
      <div class="row"><span class="field">First Name</span><span class="field">Company Name</span></div>
      <div class="row"><span class="field">Enter Email</span></div>
      <span class="btn">Subscribe &raquo;</span>
    </div>
    <ul class="links">
      <h5>Quick Links</h5>
      <li>- Home</li><li>- About Us</li><li>- Expertise</li><li>- Global Outlook</li><li>- Sectors</li><li>- Management</li><li>- Media</li><li>- Contact Us</li>
    </ul>
    <ul class="links s2">
      <h5>Sectors</h5>
      <li>- Real Estate</li><li>- E-Commerce</li><li>- Healthcare</li><li>- Beauty &amp; Personal Care</li><li>- Technology</li><li>- Resources</li>
    </ul>
    <div class="brand">
      <div class="logo"><span class="mark"></span>Meridale</div>
      <div class="social"><i></i><i></i><i></i><i></i><i></i></div>
    </div>
  </div>
  <div class="copy">&copy; 2020 Meridale Holding Partners. All Rights Reserved.</div>
</footer>

</body>
</html>
```